Host Home Needed Flier

We need a refresh of this flier to be more modern and informative. We'll use the new flier as a template for all our centers across the United States-therefore, it should be editable. We don't typically use stock photos (in order to look authentic to our clients) be would be open to a stock photo if it was relevant. We have a lot of work coming up and would like to establish a relationship with a designer. We are an international company who have been business for over 30 years working with international students ages 8-30. Our marketing/branding colors should be fresh and appeal to young people from all over the globe. We love the color blue in every shade and we love innovative cool fonts.

```html
<!DOCTYPE html>
<html lang="en">
<head>
<meta charset="utf-8">
<title>Host Home Needed Flier</title>
<link rel="stylesheet" href="https://fonts.googleapis.com/css2?family=Rubik:wght@700&family=Roboto:wght@400;700&family=Montserrat:wght@600;700&family=Zilla+Slab:wght@600;700&display=swap">
<style>
  :root{
    --page-bg:#0a4db3;
    --navy:#0d3a86;
    --ink:#0f2f6b;
    --sky:#2ea7e0;
    --white:#ffffff;
    --panel:rgba(222,228,236,0.72);
    --wash:rgba(255,255,255,0.5);
  }
  html,body{margin:0;padding:0;width:1200px;height:1013px;overflow:hidden;background:var(--page-bg);}
  .flier{position:absolute;left:236px;top:30px;width:727px;height:953px;overflow:hidden;background:var(--navy);box-shadow:0 20px 60px rgba(0,0,0,.35);}
  .side-band{position:absolute;left:0;top:0;width:129px;height:100%;background:var(--navy);}
  .sky{position:absolute;left:129px;top:0;width:598px;height:100%;
    background:linear-gradient(180deg,#dbe6f1 0%,#cfdff0 50%,#b7cfe6 70%,#9fbcdc 100%);}
  .photo{position:absolute;left:129px;top:500px;width:598px;height:453px;
    background:
      linear-gradient(180deg,rgba(190,210,232,0) 0%,rgba(190,210,232,0) 18%,rgba(40,60,110,.25) 60%,rgba(20,40,90,.55) 100%),
      linear-gradient(90deg,#3a5aa8 0%,#3657a6 18%,#c9d6e6 22%,#d5dfeb 40%,#26365f 46%,#2a3d6e 62%,#1c2a52 68%,#1d2b55 100%);
    opacity:.92;}
  .overlays{position:absolute;left:129px;top:0;width:598px;height:953px;}
  .brand-mark{position:absolute;left:62px;top:55px;width:69px;height:69px;box-sizing:border-box;background:var(--navy);border:2px solid var(--white);}
  .brand-bar{position:absolute;left:131px;top:55px;width:542px;height:69px;background:rgba(255,255,255,.92);box-sizing:border-box;padding:12px 0 0 14px;}
  .brand-name{margin:0;font:700 23px/1 "Montserrat",sans-serif;color:var(--ink);letter-spacing:.8px;}
  .brand-tagline{margin:7px 0 0;font:600 15px/1 "Montserrat",sans-serif;color:var(--ink);letter-spacing:.3px;}
  .headline{position:absolute;left:143px;top:143px;margin:0;font:700 41px/49px "Rubik",sans-serif;color:var(--ink);letter-spacing:-.3px;}
  .headline .accent{color:var(--sky);}
  .offer{position:absolute;left:143px;top:332px;margin:0;font:400 28px/34px "Roboto",sans-serif;color:var(--ink);}
  .offer b{font-weight:700;}
  .phone-text{position:absolute;right:20px;top:822px;margin:0;font:600 44px/50px "Zilla Slab",serif;color:var(--ink);}
  .web-band{position:absolute;right:0;top:882px;width:539px;height:54px;background:var(--navy);}
  .web-text{position:absolute;right:20px;top:884px;margin:0;font:700 40px/50px "Zilla Slab",serif;color:var(--white);}
</style>
</head>
<body>
<main class="flier">
  <div class="side-band"></div>
  <div class="sky"></div>
  <div class="photo" role="img" aria-label="Photo of four smiling young international students sitting side by side outdoors under a bright sky"></div>
  <svg class="overlays" viewBox="0 0 598 953" aria-hidden="true">
    <polygon points="0,0 598,0 598,128 267,584 0,584" fill="var(--wash)"/>
    <polygon points="0,316 460,316 370,453 0,453" fill="var(--panel)"/>
    <polygon points="278,819 598,819 598,873 240,873" fill="var(--white)"/>
  </svg>
  <div class="brand-mark"></div>
  <header class="brand-bar">
    <p class="brand-name">GLOBAL HOMESTAY NETWORK</p>
    <p class="brand-tagline">Remarkable American Experiences for International Students</p>
  </header>
  <h1 class="headline"><span class="accent">BECOME</span> A HOST<br>FOR AN INTERNATIONAL<br>STUDENT <span class="accent">TODAY!</span></h1>
  <p class="offer">International students<br>attending <b>HBIS</b> arriving <b>NOW!</b><br>Hosts paid <b>$1000/month</b></p>
  <p class="phone-text">555-013-4782</p>
  <div class="web-band"></div>
  <p class="web-text">www.ghnhomestays.com</p>
</main>
</body>
</html>
```